Brevant Business Card

I have a business that is called "Brevant Electrical Products LTD" My company deals with top of the range laptops and mobile phones that are exclusive. I need a business card that will be eye catching but not over complicated.

Target Market(s)

Adults aged 19 to 50
Upper middle class

Industry/Entity Type

Business

Requirements
Must have
• Company name/logo (file attached)
• It must have my contact information which is:

• Name: Dale Marwick

• Position: Managing Director 

• Business Address: 7 Hapton Row, London, W4 9QD

• Contact Number: 02085193604
• Mobile: 07814260537
• Email: info@brevant-goods.co.uk
Nice to have
• Simple and stylish
• Eye catching

```html
<!DOCTYPE html>
<html lang="en">
<head>
<meta charset="utf-8">
<title>Brevant Business Card</title>
<link rel="stylesheet" href="https://fonts.googleapis.com/css2?family=Arimo:wght@400&family=Cormorant+Garamond:ital,wght@1,700&display=swap">
<style>
  :root {
    --bg: #e9e9e9;
    --card-white: #ffffff;
    --sky-light: #e6f5fb;
    --sky-mid: #bfe4f3;
    --sky-deep: #1c9fd6;
    --brand-blue: #25a3d8;
    --brand-subtle: #3c86a8;
    --title-blue: #7a9cb8;
    --rule: #d6e2ea;
    --photo-dark: #3a3d42;
    --photo-mid: #8b9096;
    --photo-light: #c9ccd0;
  }
  * { box-sizing: border-box; margin: 0; padding: 0; }
  html, body {
    width: 1200px; height: 486px; overflow: hidden;
    background: var(--bg);
    font-family: "Arimo", Arial, sans-serif;
  }
  .card {
    position: absolute;
    top: 106px;
    width: 512px;
    height: 304px;
    overflow: hidden;
    box-shadow: 0 2px 6px rgba(0,0,0,0.18);
  }
  .card--front {
    left: 92px;
    background: linear-gradient(160deg, var(--card-white) 35%, var(--sky-light) 65%, var(--sky-mid) 100%);
  }
  .card--back {
    left: 632px;
    background: linear-gradient(180deg, var(--card-white) 20%, var(--sky-light) 55%, var(--sky-mid) 78%, var(--sky-deep) 100%);
  }
  .product-photo {
    position: absolute;
    inset: 0;
    clip-path: polygon(32% 0, 100% 0, 100% 100%, 62% 100%, 23% 48%);
    background: linear-gradient(135deg, var(--photo-dark) 0%, var(--photo-mid) 55%, var(--photo-light) 100%);
  }
  .brand {
    position: absolute;
    left: 10px;
    bottom: 14px;
    color: var(--brand-blue);
  }
  .brand__name {
    font-size: 46px;
    line-height: 1;
    letter-spacing: 1px;
    font-weight: 400;
  }
  .brand__tagline {
    margin-top: 4px;
    font-size: 17px;
    letter-spacing: 1px;
    color: var(--brand-subtle);
  }
  .person {
    position: absolute;
    top: 30px;
    left: 0; right: 0;
    text-align: center;
  }
  .person__name {
    font-size: 27px;
    color: var(--brand-blue);
    letter-spacing: 0.5px;
    font-weight: 400;
  }
  .person__rule {
    width: 260px;
    height: 1px;
    margin: 5px auto 5px;
    background: var(--rule);
  }
  .person__title {
    font-family: "Cormorant Garamond", Georgia, serif;
    font-style: italic;
    font-weight: 700;
    font-size: 18px;
    color: var(--title-blue);
  }
  .contact {
    position: absolute;
    left: 30px;
    right: 30px;
    top: 203px;
    height: 120px;
    background: var(--card-white);
    border-radius: 10px;
    padding-top: 16px;
    text-align: center;
    color: var(--brand-blue);
    font-size: 15px;
    line-height: 19px;
    font-style: normal;
  }
</style>
</head>
<body>
  <section class="card card--front">
    <div class="product-photo" role="img" aria-label="Photo of a smartphone with stylus resting on a laptop keyboard"></div>
    <div class="brand">
      <div class="brand__name">BREVANT</div>
      <div class="brand__tagline">Electrical Products</div>
    </div>
  </section>

  <section class="card card--back">
    <div class="person">
      <h1 class="person__name">DALE MARWICK</h1>
      <div class="person__rule"></div>
      <p class="person__title">Managing Director</p>
    </div>
    <address class="contact">
      Business Address: 7 Hapton Row, London, W4 9QD<br>
      Contact Number: 02085193604<br>
      Mobile: 07814260537<br>
      Email: info@brevant-goods.co.uk
    </address>
  </section>
</body>
</html>
```